Web design for community centre - bright colours (provided) and matching existing logo

Website based on a provided logo and existing website template skeleton (it is a Wordpress theme we must use that is already installed)

Basically, see if you can improve the existing theme skeleton at https://tarvoshub.org.au/redesign/. Mostly we are looking for a much nicer menu that works with the logo, and a nice font/design for text content.

We have a developer who will work your design into the Wordpress theme – so you can get creative in a graphic software app and our developer can most likely implement your ideas.

The website ideally will include design ideas from the logo (e.g. the idea of people with their arms around each other, colours).

Improvement to the text displayed on the photo slider (e.g. a colour border or other decoration) is also needed.

It needs a 'community' feel.

Target Market(s)

Parents (provides childcare), older people, people with disabilities, recent migrants

Industry/Entity Type

Community Center

Number of Pages Required

1 page

Font styles to use
Sans Serif

Colors

Designer to choose colors to be used in the design.

Requirements
Must have
• A very aesthetic top menu. Nice use of spacing, negative space etc.
• Fonts need to be legally available without a pageview fee (one off purchase OK). You need to provide proof we can use the font legally.
• See https://www.plover.org.au/ for an example of a menu we like.
• Must use the existing logo, provided in this brief.
• Needs to use colours from the logo but do not need to use all of them!
• Must be workable into the theme already installed at https://tarvoshub.org.au/redesign
Nice to have
• Maybe some kind of shapes attached to each menu link (top menu0
• A use of all 5 colours on the top menu, when you hover on it
Should not have
• Serif fonts

```html
<!DOCTYPE html>
<html lang="en">
<head>
<meta charset="utf-8">
<title>Tarvos Neighbourhood Learning Centre</title>
<link href="https://fonts.googleapis.com/css2?family=Exo+2:wght@500;600;700;800&family=Catamaran:wght@400;500;600&display=swap" rel="stylesheet">
<style>
:root{
  --blue:#1a98e0;
  --pink:#e3066a;
  --green:#77bd2f;
  --purple:#5a1f85;
  --orange:#f58220;
  --ink:#1e1e1e;
  --muted:#666;
  --page:#f1f1f1;
  --line:#dcdcdc;
  --white:#fff;
}
*{box-sizing:border-box;margin:0;padding:0}
html,body{width:1200px;height:3038px;overflow:hidden}
body{position:relative;background:var(--page);font-family:"Catamaran",sans-serif;color:var(--ink)}
.abs{position:absolute}
h1,h2,h3,h4{font-family:"Exo 2",sans-serif}

/* header */
.site-header{left:0;top:0;width:1200px;height:142px;background:var(--white)}
.brand{left:143px;top:10px;display:flex;align-items:center;gap:12px}
.brand-dot{width:70px;height:70px;border-radius:50%;background:var(--blue)}
.brand-name{font-family:"Exo 2",sans-serif;font-weight:600;font-size:21px;line-height:21px;color:var(--ink)}
.main-nav{left:143px;top:110px;display:flex;font-size:13.5px;letter-spacing:.3px;color:#333}
.main-nav a{position:relative;text-decoration:none;color:inherit;margin-right:30px}
.main-nav a.current{color:var(--orange)}
.nav-mark{left:143px;top:94px}
.search-icon{left:1024px;top:111px}

/* hero */
.hero{left:144px;top:190px;width:558px;height:401px;background:linear-gradient(180deg,#a07a36 0%,#7a5524 45%,#3a2410 100%)}
.hero-caption{left:0;bottom:0;width:558px;height:141px;background:rgba(20,16,12,.72)}
.hero-bar{left:0;top:0;width:345px;height:4px;background:var(--orange)}
.hero-title{left:0;top:20px;width:345px;text-align:center;color:var(--white);font-weight:800;font-size:34px}
.hero-text{left:0;top:72px;width:345px;text-align:center;color:var(--white);font-size:16px;line-height:23px}
.hero-arrow{top:180px;width:44px;height:42px;background:rgba(20,20,20,.75);display:flex;align-items:center;justify-content:center}

/* sidebar */
.sidebar{left:722px;top:190px;width:333px;height:401px;background:var(--white);box-shadow:0 1px 4px rgba(0,0,0,.12)}
.social-box{left:21px;top:18px;width:292px;height:171px;border:1px solid var(--line);background:#f7f7f7}
.social-box h3{position:absolute;left:0;top:34px;width:100%;text-align:center;font-weight:500;font-size:26px}
.social-row{left:56px;top:88px;display:flex;gap:6px}
.social-row span{width:40px;height:40px;display:block}
.sidebar h4{left:32px;top:214px;font-weight:500;font-size:26px}
.email-field{left:33px;top:262px;width:268px;height:42px;background:var(--white);box-shadow:0 1px 5px rgba(0,0,0,.18);font-size:13px;color:#555;padding:13px 16px}
.btn-subscribe{left:33px;top:313px;width:138px;height:42px;background:var(--orange);color:var(--white);font-family:"Exo 2",sans-serif;font-weight:700;font-size:16px;display:flex;align-items:center;justify-content:center;box-shadow:0 2px 4px rgba(0,0,0,.15)}

/* courses */
.courses{left:144px;top:614px;width:912px;height:1053px;background:var(--white);border:1px solid var(--line)}
.section-title{width:100%;text-align:center;font-weight:800;font-size:40px}
.card{width:269px;height:387px;border:3px solid;box-shadow:0 14px 10px -8px rgba(0,0,0,.35)}
.card-photo{left:0;top:0;width:263px;height:176px}
.card-icon{left:100px;top:146px;width:62px;height:62px;border-radius:50%}
.card-title{left:10px;top:222px;width:243px;text-align:center;color:var(--white);font-weight:700;font-size:20px;line-height:23px}
.card-text{left:20px;width:223px;text-align:center;color:var(--white);font-size:12.5px;line-height:19px}
.card-btn{left:82px;top:332px;width:101px;height:29px;background:var(--white);font-family:"Exo 2",sans-serif;font-weight:700;font-size:13px;display:flex;align-items:center;justify-content:center}
.blue{border-color:var(--blue);background:var(--blue)}
.pink{border-color:var(--pink);background:var(--pink)}
.green{border-color:var(--green);background:var(--green)}
.purple{border-color:var(--purple);background:var(--purple)}
.btn-outline{left:340px;top:963px;width:232px;height:42px;border:2px solid var(--orange);color:var(--orange);font-family:"Exo 2",sans-serif;font-weight:700;font-size:16px;display:flex;align-items:center;justify-content:center}

/* welcome */
.mark{width:72px;height:72px;border-radius:50%;left:564px}
.welcome-title{left:0;top:1790px;width:1200px;text-align:center;font-weight:800;font-size:40px}
.welcome-lead{left:0;top:1858px;width:1200px;text-align:center;color:var(--orange);font-family:"Exo 2",sans-serif;font-weight:600;font-size:17px}
.welcome-body{left:230px;top:1890px;width:740px;text-align:center;color:var(--muted);font-size:14.5px;line-height:32px}
.btn{height:42px;color:var(--white);font-family:"Exo 2",sans-serif;font-weight:700;font-size:17px;display:flex;align-items:center;justify-content:center}

/* upcoming */
.upcoming{left:0;top:2166px;width:1200px;height:540px;background:var(--white)}
.event{width:218px;text-align:center}
.event-photo{width:218px;height:174px}
.event h4{margin-top:14px;font-weight:600;font-size:19px;line-height:23px}
.event p{margin-top:5px;font-size:12.5px;color:#555}

/* footer */
.site-footer{left:0;top:2706px;width:1200px;height:332px;background:var(--blue);color:var(--white)}
.footer-brand{left:147px;top:54px;display:flex;align-items:center;gap:10px}
.footer-brand .brand-dot{width:70px;height:70px;background:var(--white)}
.footer-brand .brand-name{color:var(--white)}
.badge{top:149px;height:48px;background:var(--white)}
.footer h5,.site-footer h5{font-family:"Exo 2",sans-serif;font-weight:700;font-size:20px;letter-spacing:.3px}
.underline{width:40px;height:2px;background:var(--orange)}
.contact-line{display:flex;align-items:center;gap:8px;font-size:15.5px}
.ring{width:34px;height:34px;border:1.5px solid var(--white);border-radius:50%}
.footer-rule{left:144px;top:246px;width:912px;height:1px;background:rgba(255,255,255,.45)}
.legal{left:0;width:1200px;text-align:center;font-size:12.5px}
</style>
</head>
<body>

<header class="site-header abs">
  <div class="brand abs">
    <span class="brand-dot"></span>
    <div class="brand-name">Tarvos<br>Neighbourhood<br>Learning Centre</div>
  </div>
  <svg class="nav-mark abs" width="38" height="14" viewBox="0 0 38 14"><path d="M3 12 Q19 -2 35 12" fill="none" stroke="var(--green)" stroke-width="4" stroke-linecap="round"/></svg>
  <nav class="main-nav abs">
    <a class="current">HOME</a>
    <a>COURSES</a>
    <a>SOCIAL ENTERPRISE</a>
    <a>COMMUNITY PROGRAMS</a>
    <a>TARVOS CARES</a>
    <a>VENUE HIRE</a>
    <a>OPENSEAT CAFÉ</a>
  </nav>
  <svg class="search-icon abs" width="15" height="15" viewBox="0 0 15 15"><circle cx="6" cy="6" r="4.5" fill="none" stroke="var(--purple)" stroke-width="2.2"/><line x1="9.5" y1="9.5" x2="14" y2="14" stroke="var(--purple)" stroke-width="2.4"/></svg>
</header>

<section class="hero abs" role="img" aria-label="Photo of a community group performing together in a classroom">
  <div class="hero-arrow abs" style="left:0"><svg width="12" height="18"><path d="M9 2 L3 9 L9 16" fill="none" stroke="#fff" stroke-width="2"/></svg></div>
  <div class="hero-arrow abs" style="right:0"><svg width="12" height="18"><path d="M3 2 L9 9 L3 16" fill="none" stroke="#fff" stroke-width="2"/></svg></div>
  <div class="hero-caption abs">
    <span class="hero-bar abs"></span>
    <h1 class="hero-title abs">Welcome to TNLC</h1>
    <p class="hero-text abs">We provide courses for everyone<br>in the community</p>
  </div>
</section>

<aside class="sidebar abs">
  <div class="social-box abs">
    <h3>Social Media</h3>
    <div class="social-row abs">
      <span style="background:#2d3f82" aria-label="Social link"></span>
      <span style="background:#3a5f8d" aria-label="Social link"></span>
      <span style="background:#58a6e8" aria-label="Social link"></span>
      <span style="background:#3bb7ea" aria-label="Social link"></span>
    </div>
  </div>
  <h4 class="abs">Email Newsletter</h4>
  <div class="email-field abs">Email Address</div>
  <div class="btn-subscribe abs">SUBSCRIBE</div>
</aside>

<section class="courses abs">
  <h2 class="section-title abs" style="top:36px">Our Courses</h2>

  <article class="card blue abs" style="left:25px;top:116px">
    <div class="card-photo abs" role="img" aria-label="Photo of children coding at computers" style="background:linear-gradient(135deg,#c9c4bd,#7e8a94)"></div>
    <span class="card-icon abs" style="background:var(--blue)"><svg width="62" height="62"><circle cx="31" cy="31" r="14" fill="none" stroke="#fff" stroke-width="2"/></svg></span>
    <h3 class="card-title abs">Kids Coding Club</h3>
    <p class="card-text abs" style="top:260px">A fun filled introduction to Computer Programming for Children in Grades 2 to 6. These</p>
    <span class="card-btn abs" style="color:var(--blue)">READ MORE</span>
  </article>

  <article class="card pink abs" style="left:320px;top:116px">
    <div class="card-photo abs" role="img" aria-label="Photo of hands typing on a keyboard" style="background:linear-gradient(135deg,#6a4a3a,#c9b8a8)"></div>
    <span class="card-icon abs" style="background:var(--pink)"><svg width="62" height="62"><rect x="19" y="18" width="24" height="20" fill="none" stroke="#fff" stroke-width="2"/><line x1="16" y1="43" x2="46" y2="43" stroke="#fff" stroke-width="2"/></svg></span>
    <h3 class="card-title abs">Digital Literacy for EAL</h3>
    <p class="card-text abs" style="top:260px">Update your digital literacy in a supportive environment whilst improving your language skills.</p>
    <span class="card-btn abs" style="color:var(--pink)">READ MORE</span>
  </article>

  <article class="card green abs" style="left:616px;top:116px">
    <div class="card-photo abs" role="img" aria-label="Photo of a young boy reading a book" style="background:linear-gradient(135deg,#3f4a5c,#8b93a0)"></div>
    <span class="card-icon abs" style="background:var(--green)"><svg width="62" height="62"><circle cx="31" cy="24" r="7" fill="none" stroke="#fff" stroke-width="2"/><path d="M19 44 L31 38 L43 44 L43 34 L31 30 L19 34 Z" fill="none" stroke="#fff" stroke-width="2"/></svg></span>
    <h3 class="card-title abs">Little Readers – Prep -Year 6</h3>
    <p class="card-text abs" style="top:282px">The program covers 70 spelling codes (sounds) found in the English language.</p>
    <span class="card-btn abs" style="color:var(--green)">READ MORE</span>
  </article>

  <article class="card green abs" style="left:25px;top:532px">
    <div class="card-photo abs" role="img" aria-label="Photo of a hand writing business notes in a notebook" style="background:linear-gradient(135deg,#e8e4de,#5a3a2a)"></div>
    <span class="card-icon abs" style="background:var(--green)"><svg width="62" height="62"><circle cx="31" cy="31" r="15" fill="none" stroke="#fff" stroke-width="2"/><circle cx="31" cy="31" r="6" fill="none" stroke="#fff" stroke-width="2"/></svg></span>
    <h3 class="card-title abs">Small business start-up</h3>
    <p class="card-text abs" style="top:260px">Have you got ideas for starting up a new business and don't know where to start?The course will introduce</p>
    <span class="card-btn abs" style="color:var(--green)">READ MORE</span>
  </article>

  <article class="card purple abs" style="left:320px;top:532px">
    <div class="card-photo abs" role="img" aria-label="Photo of older learners at computers in a classroom" style="background:linear-gradient(135deg,#9a8c80,#4a4440)"></div>
    <span class="card-icon abs" style="background:var(--purple)"><svg width="62" height="62"><rect x="18" y="18" width="26" height="19" fill="none" stroke="#fff" stroke-width="2"/><line x1="25" y1="43" x2="37" y2="43" stroke="#fff" stroke-width="2"/></svg></span>
    <h3 class="card-title abs">IT for Beginners</h3>
    <p class="card-text abs" style="top:260px">Created for those who would like to develop their computer skills and gain confidence in using the internet,</p>
    <span class="card-btn abs" style="color:var(--purple)">READ MORE</span>
  </article>

  <article class="card blue abs" style="left:616px;top:532px">
    <div class="card-photo abs" role="img" aria-label="Photo of students painting in an art class" style="background:linear-gradient(135deg,#8a8078,#c8beb2)"></div>
    <span class="card-icon abs" style="background:var(--blue)"><svg width="62" height="62"><path d="M20 44 L42 44 L40 32 L22 32 Z" fill="none" stroke="#fff" stroke-width="2"/><line x1="26" y1="32" x2="24" y2="18" stroke="#fff" stroke-width="2"/><line x1="32" y1="32" x2="33" y2="16" stroke="#fff" stroke-width="2"/><line x1="37" y1="32" x2="41" y2="19" stroke="#fff" stroke-width="2"/></svg></span>
    <h3 class="card-title abs">Mixed Media Art class ages 13-17</h3>
    <p class="card-text abs" style="top:282px">Consolidating technique with life drawing sessions followed by 2D &amp;3D projects.</p>
    <span class="card-btn abs" style="color:var(--blue)">READ MORE</span>
  </article>

  <a class="btn-outline abs">VIEW ALL COURSES</a>
</section>

<span class="mark abs" style="top:1708px;background:var(--orange)"></span>
<h2 class="welcome-title abs">Welcome to TNLC</h2>
<p class="welcome-lead abs">We provide courses for everyone in the community</p>
<p class="welcome-body abs">Sed ut perspiciatis unde omnis iste natus error sit voluptatem accusantium doloremque laudantium, totam rem aperiam, eaque ipsa quae ab illo inventore veritatis et quasi architecto beatae vitae dicta sunt explicaemo enim ipsam voluptatem quia voluptas sit aspernatur aut odit aut fugit, sed quia consequi dolorem ipsum quia dolor sit amet, consectetuquuntur magni dolores eos qui ratione voluptatem</p>
<a class="btn abs" style="left:402px;top:2040px;width:232px;background:var(--orange)">View Course Brochure</a>
<a class="btn abs" style="left:647px;top:2040px;width:151px;background:var(--purple)">Enrol Now</a>

<section class="upcoming abs">
  <span class="mark abs" style="top:45px;background:var(--pink)"></span>
  <h2 class="section-title abs" style="top:128px">Courses starting soon</h2>
  <svg class="abs" style="left:80px;top:256px" width="28" height="90"><path d="M26 2 L3 45 L26 88" fill="none" stroke="#9a9a9a" stroke-width="2"/></svg>
  <svg class="abs" style="left:1092px;top:256px" width="28" height="90"><path d="M2 2 L25 45 L2 88" fill="none" stroke="#9a9a9a" stroke-width="2"/></svg>

  <div class="event abs" style="left:143px;top:212px">
    <div class="event-photo" role="img" aria-label="Photo of latte art being poured into a cup" style="background:linear-gradient(135deg,#3a3a4a,#d8b48a)"></div>
    <h4>Barista Training</h4><p>Monday 16th September</p>
  </div>
  <div class="event abs" style="left:375px;top:212px">
    <div class="event-photo" role="img" aria-label="Photo of an exercise class with a ball" style="background:linear-gradient(135deg,#e0a850,#c07a30)"></div>
    <h4>Mara's class for<br>the young at Heart</h4><p>Monday 7th October</p>
  </div>
  <div class="event abs" style="left:607px;top:212px">
    <div class="event-photo" role="img" aria-label="Photo of someone playing a ukulele" style="background:linear-gradient(135deg,#8a94a4,#5a4a3a)"></div>
    <h4>Ukulele</h4><p>Monday 7th October</p>
  </div>
  <div class="event abs" style="left:839px;top:212px">
    <div class="event-photo" role="img" aria-label="Collage of classroom photos" style="background:linear-gradient(135deg,#d8d8d8,#6a6a72)"></div>
    <h4>EAL</h4><p>Monday 7th October</p>
  </div>
</section>

<footer class="site-footer abs">
  <div class="footer-brand abs">
    <span class="brand-dot"></span>
    <div class="brand-name">Tarvos<br>Neighbourhood<br>Learning Centre</div>
  </div>
  <span class="badge abs" style="left:147px;width:62px" aria-label="Partner badge"></span>
  <span class="badge abs" style="left:215px;width:62px" aria-label="Partner badge"></span>
  <span class="badge abs" style="left:284px;width:62px;background:#0a3b7a" aria-label="Partner badge"></span>

  <h5 class="abs" style="left:455px;top:50px">CONTACT INFO</h5>
  <span class="underline abs" style="left:455px;top:82px"></span>
  <div class="contact-line abs" style="left:455px;top:102px">
    <svg width="13" height="13" viewBox="0 0 13 13"><path d="M2 1 L5 1 L6 4 L4 5 Q5 8 8 9 L9 7 L12 8 L12 11 Q7 12 4 9 Q1 6 2 1 Z" fill="#fff"/></svg>Phone: 03 9000 4172
  </div>
  <div class="contact-line abs" style="left:455px;top:132px">
    <svg width="10" height="14" viewBox="0 0 10 14"><path d="M5 0 A5 5 0 0 1 10 5 Q10 8 5 14 Q0 8 0 5 A5 5 0 0 1 5 0 Z" fill="#fff"/><circle cx="5" cy="5" r="2" fill="var(--blue)"/></svg>4-10 Alder St,Tarvos VIC 3999
  </div>
  <div class="abs" style="left:455px;top:175px;display:flex;gap:6px">
    <span class="ring"></span><span class="ring"></span><span class="ring"></span><span class="ring"></span>
  </div>

  <h5 class="abs" style="left:734px;top:50px">SIGN UP NEWSLETTER</h5>
  <span class="underline abs" style="left:734px;top:82px"></span>
  <p class="abs" style="left:736px;top:102px;font-size:15.5px">Sed ut perspiciatis unde omnis iste natus error</p>
  <div class="abs" style="left:736px;top:137px;width:218px;height:34px;background:#fff;color:#444;font-size:13px;padding:9px 12px">Enter Email</div>
  <div class="abs" style="left:954px;top:137px;width:97px;height:34px;background:var(--orange);font-family:'Exo 2',sans-serif;font-weight:700;font-size:12.5px;display:flex;align-items:center;justify-content:center">SUBSCRIBE</div>

  <span class="footer-rule abs"></span>
  <p class="legal abs" style="top:272px">© 2019 Tarvos Neighbourhood Learning Centre. All Rights Reserved. Policies &amp; Procedures.</p>
  <p class="legal abs" style="top:295px">Tarvos Neighbourhood Learning Centre Inc is registered as a charity with the Australian Charities and Not-for-profits Commission ABN 12 345 678 901.</p>
</footer>

</body>
</html>
```